Postcard Design

Name of the Company is : Harbor Lantern Sport Fishing Charters Block Island RI
Name of the boat : Reel Tide Joy
local Captain Dennis Hartwell
pricing and booking : 401-555-0193
We specialize in:

Shark & Tuna Trips
Full or half day Inshore Bass & Bluefish
Half day bottom fishing for Fluke, Sea Bass & Scup
Inshore night fishing trips
Custom Combination Charters also available
Our crew provides:
A professional and accommodating experience
A very child friendly environment
A range of technique options for every style of trip
An immense knowledge of the waters.
Our Vessel:
Meets all NMSA safety requirement
Twin 250 Hp Valdrek Turbo Diesels
All updated electronics
On the comfort side : we have a restroom, and a galley area with a table so you can enjoy your lunch.

Payments : We except; Cash , Check , Kp, Tz, Rl and Nb

I have attached the logo I would like to use . If possible I would like to use the banners on the logo with Company Name & number.

```html
<!DOCTYPE html>
<html lang="en">
<head>
<meta charset="utf-8">
<title>Harbor Lantern Sport Fishing Charters – Postcard</title>
<link rel="stylesheet" href="https://fonts.googleapis.com/css2?family=Oswald:wght@500&family=Lato:wght@400;700&display=swap">
<style>
  :root{
    --navy:#14284d;
    --navy-deep:#0f1f3d;
    --stripe:#3d6eb5;
    --gold:#e9a425;
    --gold-dark:#d58f14;
    --white:#ffffff;
    --page:#f1f1f1;
    --sky:#e6ebef;
    --sea:#3d6a95;
  }
  *{box-sizing:border-box;margin:0;padding:0}
  html,body{width:1200px;height:1200px;overflow:hidden;background:var(--page)}
  .postcard{
    position:absolute;left:129px;top:220px;width:946px;height:732px;
    overflow:hidden;background:var(--white);
    font-family:"Lato",sans-serif;color:var(--white);
  }
  .photo-area{
    position:absolute;left:420px;top:0;width:526px;height:660px;
    background:linear-gradient(172deg,var(--sky) 0%,var(--sky) 28%,#c9d4de 42%,var(--sea) 72%,#2c5479 100%);
  }
  .panel-stripe{
    position:absolute;inset:0;background:var(--stripe);
    clip-path:polygon(0 0,622px 0,502px 100%,0 100%);
  }
  .panel{
    position:absolute;inset:0;
    background:linear-gradient(180deg,var(--navy) 0%,#1a3560 60%,var(--navy-deep) 100%);
    clip-path:polygon(0 0,612px 0,492px 100%,0 100%);
  }
  .panel-footer{
    position:absolute;left:0;top:512px;width:100%;height:220px;background:var(--navy-deep);
    clip-path:polygon(0 0,542px 0,492px 220px,0 220px);
  }
  .glow-line{
    position:absolute;left:0;top:510px;width:520px;height:2px;
    background:linear-gradient(90deg,rgba(255,255,255,.1),rgba(255,255,255,.9) 45%,rgba(255,255,255,.1));
  }
  .section-title{
    position:absolute;left:48px;font-family:"Oswald",sans-serif;font-weight:500;
    font-size:25px;letter-spacing:.5px;color:var(--gold);text-transform:uppercase;
  }
  .checklist{position:absolute;left:48px;list-style:none}
  .checklist li{
    display:flex;align-items:center;height:22.7px;font-size:15.5px;letter-spacing:.35px;
  }
  .checklist svg{width:14px;height:14px;margin-right:18px;flex:none}
  .boat-info{position:absolute;left:46px;top:524px;font-size:14px;line-height:21px;letter-spacing:.3px}
  .booking{
    position:absolute;left:46px;top:574px;font-weight:700;
    font-size:19px;color:var(--gold);letter-spacing:.3px;
  }
  .booking span{color:var(--white)}
  .payments{position:absolute;left:46px;top:614px;display:flex;align-items:center;font-size:14px;letter-spacing:.3px}
  .payments svg{width:42px;height:30px;margin-right:17px}
  .comfort-bar{
    position:absolute;left:0;top:660px;width:100%;height:48px;
    background:linear-gradient(180deg,var(--gold) 0%,var(--gold-dark) 100%);
    display:flex;align-items:center;justify-content:center;
    font-family:"Oswald",sans-serif;font-weight:500;font-size:22px;letter-spacing:.5px;
    text-transform:uppercase;color:var(--white);
  }
  .brand{
    position:absolute;left:640px;top:62px;width:290px;
    display:flex;align-items:center;gap:12px;
  }
  .brand-dot{width:20px;height:20px;border-radius:50%;background:var(--gold);flex:none}
  .brand-name{
    font-family:"Oswald",sans-serif;font-weight:500;font-size:23px;line-height:28px;
    color:var(--navy);text-transform:uppercase;
  }
</style>
</head>
<body>
<main class="postcard">
  <div class="photo-area" role="img" aria-label="Photo of an angler on a boat deck bending a fishing rod over the open sea"></div>
  <div class="panel-stripe"></div>
  <div class="panel"></div>
  <div class="panel-footer"></div>
  <div class="glow-line"></div>

  <div class="brand">
    <div class="brand-dot"></div>
    <div class="brand-name">Harbor Lantern Sport Fishing Charters</div>
  </div>

  <h2 class="section-title" style="top:50px">We specialize in:</h2>
  <ul class="checklist" style="top:95px">
    <li><svg viewBox="0 0 14 14"><rect x="1" y="2" width="11" height="11" fill="none" stroke="#e9a425" stroke-width="1.6"/><path d="M3.5 7l2.5 2.7L13 1.5" fill="none" stroke="#e9a425" stroke-width="2"/></svg>Shark &amp; Tuna Trips</li>
    <li><svg viewBox="0 0 14 14"><rect x="1" y="2" width="11" height="11" fill="none" stroke="#e9a425" stroke-width="1.6"/><path d="M3.5 7l2.5 2.7L13 1.5" fill="none" stroke="#e9a425" stroke-width="2"/></svg>Full or half day Inshore Bass &amp; Bluefish</li>
    <li><svg viewBox="0 0 14 14"><rect x="1" y="2" width="11" height="11" fill="none" stroke="#e9a425" stroke-width="1.6"/><path d="M3.5 7l2.5 2.7L13 1.5" fill="none" stroke="#e9a425" stroke-width="2"/></svg>Half day bottom fishing for Fluke, Sea Bass &amp; Scup</li>
    <li><svg viewBox="0 0 14 14"><rect x="1" y="2" width="11" height="11" fill="none" stroke="#e9a425" stroke-width="1.6"/><path d="M3.5 7l2.5 2.7L13 1.5" fill="none" stroke="#e9a425" stroke-width="2"/></svg>Inshore night fishing trips</li>
    <li><svg viewBox="0 0 14 14"><rect x="1" y="2" width="11" height="11" fill="none" stroke="#e9a425" stroke-width="1.6"/><path d="M3.5 7l2.5 2.7L13 1.5" fill="none" stroke="#e9a425" stroke-width="2"/></svg>Custom Combination Charters also available</li>
  </ul>

  <h2 class="section-title" style="top:216px">Our crew provides:</h2>
  <ul class="checklist" style="top:256px">
    <li><svg viewBox="0 0 14 14"><rect x="1" y="2" width="11" height="11" fill="none" stroke="#e9a425" stroke-width="1.6"/><path d="M3.5 7l2.5 2.7L13 1.5" fill="none" stroke="#e9a425" stroke-width="2"/></svg>A professional and accommodating experience</li>
    <li><svg viewBox="0 0 14 14"><rect x="1" y="2" width="11" height="11" fill="none" stroke="#e9a425" stroke-width="1.6"/><path d="M3.5 7l2.5 2.7L13 1.5" fill="none" stroke="#e9a425" stroke-width="2"/></svg>A very child friendly environment</li>
    <li><svg viewBox="0 0 14 14"><rect x="1" y="2" width="11" height="11" fill="none" stroke="#e9a425" stroke-width="1.6"/><path d="M3.5 7l2.5 2.7L13 1.5" fill="none" stroke="#e9a425" stroke-width="2"/></svg>A range of technique options for every style of trip</li>
    <li><svg viewBox="0 0 14 14"><rect x="1" y="2" width="11" height="11" fill="none" stroke="#e9a425" stroke-width="1.6"/><path d="M3.5 7l2.5 2.7L13 1.5" fill="none" stroke="#e9a425" stroke-width="2"/></svg>An immense knowledge of the waters.</li>
  </ul>

  <h2 class="section-title" style="top:362px">Our vessel:</h2>
  <ul class="checklist" style="top:403px">
    <li><svg viewBox="0 0 14 14"><rect x="1" y="2" width="11" height="11" fill="none" stroke="#e9a425" stroke-width="1.6"/><path d="M3.5 7l2.5 2.7L13 1.5" fill="none" stroke="#e9a425" stroke-width="2"/></svg>Meets all NMSA safety requirement</li>
    <li><svg viewBox="0 0 14 14"><rect x="1" y="2" width="11" height="11" fill="none" stroke="#e9a425" stroke-width="1.6"/><path d="M3.5 7l2.5 2.7L13 1.5" fill="none" stroke="#e9a425" stroke-width="2"/></svg>Twin 250 Hp Valdrek Turbo Diesels</li>
    <li><svg viewBox="0 0 14 14"><rect x="1" y="2" width="11" height="11" fill="none" stroke="#e9a425" stroke-width="1.6"/><path d="M3.5 7l2.5 2.7L13 1.5" fill="none" stroke="#e9a425" stroke-width="2"/></svg>All updated electronics</li>
  </ul>

  <div class="boat-info">
    <p>Name of the boat : Reel Tide Joy</p>
    <p>local Captain Dennis Hartwell</p>
  </div>
  <p class="booking">PRICING AND BOOKING : <span>401-555-0193</span></p>
  <div class="payments">
    <svg viewBox="0 0 42 30"><rect x="8" y="2" width="30" height="19" rx="3" fill="none" stroke="#e9a425" stroke-width="2.4"/><line x1="8" y1="8" x2="38" y2="8" stroke="#e9a425" stroke-width="2.4"/><path d="M2 14h9l6 4-3 3h-6v7H2z" fill="none" stroke="#e9a425" stroke-width="2.4" stroke-linejoin="round"/></svg>
    <p>Payments : We except; Cash , Check , Kp, Tz, Rl and Nb</p>
  </div>

  <div class="comfort-bar">We have a restroom, and a galley area with a table so you can enjoy your lunch.</div>
</main>
</body>
</html>
```